"Fight Back" banner ad design

We have sketched the design and have images to consider including. We are looking for something striking, FIGHT BACK! with a clenched fist image, then a fading images of variance.png and hi-bill.png in the background. Tag line "Fight your water bill with your own data" optionally include "Crest View" rivo3159 logo, KMPT Design, LLC based in San Diego CA. Pre-order now, visit https://www.raisenest.com/rivoplume @rivo3159, info@rivo3159.com

"Fight your water bill with your own data"

```html
<!DOCTYPE html>
<html lang="en">
<head>
<meta charset="utf-8">
<title>Fight Back – Banner</title>
<link rel="stylesheet" href="https://fonts.googleapis.com/css2?family=Open+Sans:ital,wght@0,400;0,600;0,700;1,400;1,600;1,700&family=Arimo:wght@400;700&display=swap">
<style>
  :root {
    --page: #e4e6e9;
    --navy-deep: #1c2a40;
    --navy: #2d4668;
    --navy-light: #4f6f98;
    --white: #ffffff;
    --yellow: #f2c200;
    --label-yellow: #ffcc00;
    --ink: #1a1a1a;
    --teal: #2f8a9c;
    --bill-head: #3a6f7c;
    --bill-total: #a9d4df;
    --button: #111111;
    --photo-tone: #c42a24;
    --photo-tone-dark: #8f1d1b;
  }
  * { margin: 0; padding: 0; box-sizing: border-box; }
  html, body { width: 1200px; height: 1200px; overflow: hidden; }
  body { background: var(--page); font-family: "Open Sans", Arial, sans-serif; position: relative; }

  .banner {
    position: absolute; left: 20px; top: 370px;
    width: 1160px; height: 460px;
    background: var(--white); overflow: hidden;
  }
  .banner-backdrop { position: absolute; inset: 0; width: 1160px; height: 460px; }

  .glove-photo {
    position: absolute; left: 66px; top: 31px; width: 177px; height: 315px;
    background: radial-gradient(ellipse at 50% 35%, var(--photo-tone) 0%, var(--photo-tone-dark) 100%);
    box-shadow: 0 0 36px 8px rgba(150, 200, 240, 0.3);
  }

  .headline {
    position: absolute; left: 290px; top: 40px;
    color: var(--white); font-style: italic; font-weight: 700;
    font-size: 53px; letter-spacing: 0.3px; line-height: 1;
  }
  .tagline {
    position: absolute; left: 290px; top: 100px;
    color: var(--white); font-style: italic; font-size: 26px; line-height: 1.2;
  }
  .tagline em { color: var(--yellow); font-style: italic; }

  .contact {
    position: absolute; left: 295px; top: 206px;
    color: var(--white); font-weight: 600; line-height: 1.12;
  }
  .contact .visit { font-size: 19px; margin-bottom: 5px; }
  .contact .link { font-size: 25px; letter-spacing: 0.8px; line-height: 1.16; }

  .bill {
    position: absolute; left: 829px; top: 51px; width: 213px; height: 307px;
    background: var(--white); border: 1px solid #7c8a96;
    font-family: Arimo, Arial, sans-serif; font-size: 7.4px; color: var(--ink);
    box-shadow: 0 8px 14px rgba(0,0,0,0.18);
  }
  .bill-head {
    background: var(--bill-head); color: var(--white); text-align: center;
    font-weight: 700; font-size: 8px; padding: 1px 0;
  }
  .bill-body { padding: 3px 6px 0 4px; }
  .bill-row { display: flex; justify-content: space-between; line-height: 9.4px; }
  .bill-row .cells { display: flex; gap: 6px; }
  .bill-section { font-weight: 700; margin-top: 2px; }
  .bill-gap { height: 14px; }
  .in1 { padding-left: 7px; }
  .in2 { padding-left: 16px; }
  .bill-sub { border-top: 1px solid #333; width: 40px; margin-left: auto; }
  .bill-brand {
    position: absolute; right: 12px; bottom: 26px; text-align: center;
    color: var(--teal); font-weight: 700; font-size: 11px;
  }
  .bill-brand .dot { display: block; width: 22px; height: 22px; border-radius: 50%; border: 2px solid var(--teal); margin: 0 auto 6px; }
  .bill-total {
    position: absolute; left: 0; right: 0; bottom: 0;
    background: var(--bill-total); border-top: 1px solid #333;
    display: flex; justify-content: space-between; padding: 1px 6px 1px 4px;
    font-weight: 700; font-size: 8px;
  }

  .client-brand { position: absolute; left: 22px; top: 364px; width: 104px; text-align: center; }
  .client-brand .mark { display: block; width: 46px; height: 46px; border-radius: 50%; border: 2px solid var(--navy-light); margin: 0 auto 22px; }
  .client-brand .name { font-style: italic; font-size: 14px; color: var(--navy); }

  .studio { position: absolute; left: 156px; top: 389px; }
  .studio .label {
    display: inline-block; background: var(--label-yellow); color: var(--ink);
    font-weight: 600; font-size: 18px; letter-spacing: 0.6px;
    width: 166px; height: 34px; line-height: 34px; text-align: center;
  }
  .studio .note { font-size: 12.5px; font-weight: 600; color: var(--ink); margin-top: 5px; }

  .cta {
    position: absolute; left: 824px; top: 391px; width: 224px; height: 54px;
    background: var(--button); color: var(--white); border-radius: 9px;
    display: flex; align-items: center; justify-content: center; gap: 8px;
    font-size: 22px; font-weight: 400;
    box-shadow: 0 3px 6px rgba(0,0,0,0.3);
  }
  .cta svg { width: 14px; height: 16px; }
</style>
</head>
<body>
  <section class="banner">
    <svg class="banner-backdrop" viewBox="0 0 1160 460" aria-hidden="true">
      <defs>
        <radialGradient id="navyGlow" cx="0.35" cy="0.05" r="0.9">
          <stop offset="0" stop-color="#4b6d99"/>
          <stop offset="0.55" stop-color="#2d4668"/>
          <stop offset="1" stop-color="#1c2a40"/>
        </radialGradient>
        <linearGradient id="swoosh" x1="0" y1="0" x2="1" y2="0">
          <stop offset="0" stop-color="#c9d2dc"/>
          <stop offset="1" stop-color="#ffffff"/>
        </linearGradient>
      </defs>
      <path d="M0,0 H1160 V10 C1000,160 830,300 560,340 C380,364 200,360 0,342 Z" fill="url(#swoosh)"/>
      <path d="M0,0 H1160 V0 C1000,150 830,290 560,330 C380,354 200,352 0,332 Z" fill="url(#navyGlow)"/>
    </svg>

    <div class="glove-photo" role="img" aria-label="Photo of a raised arm wearing a red boxing glove"></div>

    <h1 class="headline">FIGHT BACK!</h1>
    <p class="tagline">Fight your <em>water bill</em> with your own data</p>

    <div class="contact">
      <p class="visit">visit</p>
      <p class="link">www.raisenest.com/rivoplume</p>
      <p class="link">@rivo3159, info@rivo3159.com</p>
    </div>

    <div class="bill">
      <div class="bill-head">FEES &amp; CHARGES</div>
      <div class="bill-body">
        <div class="bill-row bill-section"><span>Water Services</span></div>
        <div class="bill-row in1"><span>Single Family Residential Base Fee</span><span>48.44</span></div>
        <div class="bill-row in1"><span class="cells"><span>Water Used</span><span>65</span><span>HCF</span></span></div>
        <div class="bill-row in2"><span class="cells"><span>Tier 1</span><span>8.00 HCF @ $4.8425</span></span><span>38.74</span></div>
        <div class="bill-row in2"><span class="cells"><span>Tier 2</span><span>16.00 HCF @ $5.4231</span></span><span>86.77</span></div>
        <div class="bill-row in2"><span class="cells"><span>Tier 3</span><span>12.00 HCF @ $7.7483</span></span><span>92.98</span></div>
        <div class="bill-row in2"><span class="cells"><span>Tier 4</span><span>29.00 HCF @</span></span><span>315.96</span></div>
        <div class="bill-row in2"><span style="padding-left:86px">$10.8952</span><span class="bill-sub"></span></div>
        <div class="bill-row in1"><span>Total Charge for Water Used</span><span>534.45</span></div>
        <div class="bill-gap"></div>
        <div class="bill-row bill-section"><span>Sewer &amp; Storm Drain Services</span></div>
        <div class="bill-row in1"><span>Sewer Base Fee</span><span>30.66</span></div>
        <div class="bill-row in1"><span>Sewer Service Charge</span><span>60.17</span></div>
        <div class="bill-row in1"><span>Storm Drain</span><span>1.90</span></div>
        <div class="bill-gap"></div>
        <div class="bill-row bill-section"><span>Total Current Charges</span><span>675.62</span></div>
        <div class="bill-row"><span>Deferred Due</span><span>79.66</span></div>
      </div>
      <div class="bill-brand"><span class="dot"></span>rivo3159</div>
      <div class="bill-total"><span>TOTAL DUE</span><span>755.28</span></div>
    </div>

    <div class="client-brand">
      <span class="mark"></span>
      <span class="name">Crest View</span>
    </div>

    <div class="studio">
      <span class="label">KMPT Design</span>
      <p class="note">LLC based in San Diego CA</p>
    </div>

    <div class="cta">
      <span>Pre Order Now!</span>
      <svg viewBox="0 0 14 16" aria-hidden="true"><path d="M1,1 L13,8 L1,15 Z" fill="#ffffff"/></svg>
    </div>
  </section>
</body>
</html>
```